One Page Menu for Food Truck centered on healthy and sustainable eating

This project is a menu for Trovik's - a mobile catering company centered around healthy and sustainable eating.

The menu will be distributed in PDF and print formats. Because of the different mediums, it needs to be one page size.

Our menu will feature three healthy wraps:

The Garden - $7
Filled with Hummus, Fresh Roasted Peppers, Sliced Cucumber, Spinach, Mint Leaves, and Za'tar. (Our vegan option)

The Steak - $8
Filled with Seared Flat Iron Steak, Caramelized Onions, and Blue Cheese.

The Mediterranean - $7
Filled with Marinated Artichoke Hearts, Kalamata Olives, Pepperoncini, and Fresh Squeezed Lemon with a Feta Cheese and Labne Spread.

Trovik's also provides:

Aquas Frescas - $3
A Refreshing Daily Blend of Fruit and Vegetable Purée, Chia Seeds, and Agave Nectar

Sierra Verde Mountain Reserve Coffee - $2

Water - $1

The design should reflect Trovik's colors of Orange and Green. We would also like a design that incorporates urban gardening, but how is up to you.

Please see website for company - trovik.org

Industry/Entity Type

Catering

Requirements
Must have
• Menu items, short descriptions, company logo, Green Colors and Orange Colors

```html
<!DOCTYPE html>
<html lang="en">
<head>
<meta charset="utf-8">
<title>Trovik's Menu</title>
<link rel="stylesheet" href="https://fonts.googleapis.com/css2?family=Arvo:ital,wght@0,700;1,400&display=swap">
<style>
  :root {
    --backdrop: #ede1c9;
    --backdrop-light: #f5ecd9;
    --frame-green: #1a9a4a;
    --band-orange: #f4d399;
    --panel: #fffdf7;
    --panel-edge: #f7f0e0;
    --text-green: #16984a;
    --brand-orange: #f28a1f;
  }
  * { margin: 0; padding: 0; box-sizing: border-box; }
  html, body { width: 925px; height: 1200px; overflow: hidden; }
  body { background: var(--backdrop); position: relative; }

  .backdrop-ornament {
    position: absolute; inset: 0;
    background: radial-gradient(ellipse at center, var(--backdrop-light) 0%, var(--backdrop) 70%);
  }

  .menu-frame {
    position: absolute; left: 128px; top: 79px; width: 674px; height: 1023px;
    border: 2px solid var(--frame-green);
    background: var(--band-orange);
    padding: 14px;
  }
  .menu-panel {
    width: 100%; height: 100%;
    background: radial-gradient(ellipse at 50% 45%, var(--panel) 0%, var(--panel) 55%, var(--panel-edge) 100%);
  }

  .brand-name {
    position: absolute; left: 160px; top: 150px; width: 610px;
    text-align: center;
    font-family: "Arvo", "Rockwell", serif; font-weight: 700;
    font-size: 124px; line-height: 1;
    color: var(--brand-orange);
  }

  .menu-item { position: absolute; left: 180px; width: 570px; }
  .item-head { display: flex; justify-content: space-between; align-items: flex-end; }
  .item-title, .item-price {
    font-family: "Arvo", "Rockwell", serif; font-weight: 700;
    font-size: 27px; line-height: 36px; color: var(--text-green);
  }
  .item-price { flex: none; }
  .item-desc {
    font-family: "Arvo", "Rockwell", serif; font-style: italic; font-weight: 400;
    font-size: 15px; line-height: 22px; color: var(--text-green);
    white-space: nowrap;
  }
  .item-garden { top: 408px; }
  .item-steak { top: 531px; }
  .item-mediterranean { top: 656px; }
  .item-aguas { top: 798px; }
  .item-coffee { top: 918px; }
  .item-water { top: 1022px; }
</style>
</head>
<body>
  <div class="backdrop-ornament" role="img" aria-label="Cream background with white flourish and leaf scroll ornament"></div>

  <div class="menu-frame"><div class="menu-panel"></div></div>

  <div class="brand-name">Trovik's</div>

  <section class="menu-item item-garden">
    <div class="item-head"><h2 class="item-title">The Garden</h2><span class="item-price">$7</span></div>
    <p class="item-desc">Filled with Hummus, Fresh Roasted Peppers, Sliced Cucumber,<br>Spinach, Mint Leaves, and Za'tar. /Our vegan option/</p>
  </section>

  <section class="menu-item item-steak">
    <div class="item-head"><h2 class="item-title">The Steak</h2><span class="item-price">$8</span></div>
    <p class="item-desc">Filled with Seared Flat Iron Steak, Caramelized Onions, and<br>Blue Cheese.</p>
  </section>

  <section class="menu-item item-mediterranean">
    <div class="item-head"><h2 class="item-title">The Mediterranean</h2><span class="item-price">$7</span></div>
    <p class="item-desc">Filled with Marinated Artichoke Hearts, Kalamata Olives,<br>Pepperoncini, and Fresh Squeezed Lemon with a Feta Cheese<br>and Labne Spread</p>
  </section>

  <section class="menu-item item-aguas">
    <div class="item-head"><h2 class="item-title">Aquas Frescas</h2><span class="item-price">$3</span></div>
    <p class="item-desc">A Refreshing Daily Blend of Fruit and Vegetable Purée, Chia<br>Seeds, and Agave Nectar</p>
  </section>

  <section class="menu-item item-coffee">
    <div class="item-head"><h2 class="item-title">Sierra Verde Mountain Reserve<br>Coffee</h2><span class="item-price">$2</span></div>
  </section>

  <section class="menu-item item-water">
    <div class="item-head"><h2 class="item-title">Water</h2><span class="item-price">$1</span></div>
  </section>
</body>
</html>
```